Bright K's Auto Detailing new business cards

I am a business owner who professionally details cars. I clean and detail the interiors, exteriors of vehicles. I need a logo designed for my new business Bright K's Auto Detailing and a great designed card that will wow anyone that I hand it out to. Attached is a photo that I would like on side of the card. I want the picture to be on the right side of the card, while my busines name will be on the other side. I want the picture to have a slant where it divided the card into left and right, not just straight down. The picture will be printed glossy and I want the left half to have a carbon fiber background. Feel free to design a cool font for the business name, The business name needs to be a red gloss to pop out against the matte background. The back of the card should have my name Colin Marchetti. Under my name should be Owner/ Operator. then all my contact info and fb and instagram stuff. must include services offered- Paint Correction, Exterior detailing
Interior Detailing, Engine Bay Detailing, Headlight restoration, Ceramic Coatings

Target Market(s)

My target market is anyone who drives a vehicle.

Industry/Entity Type

Automotive

Contact Information for Business Card

Business name- Bright K's Auto Detailing
Colin Marchetti Owner/ Operator
Location- Oakmere, CA
Business # (559) 214-6079
email- colin@thebrightpolisher.example
fb and instragram logos- @thebrightpolisher

Font styles to use
Serif
Script
Other font styles liked:
• Blacksword

Colors
ec1f27
000000

Requirements
Must have
• The card must be in landscape position. All the details that are in the brief description which are my business name, my name, services offered and any other info thats in the project description. I uploaded pics of veltranos that I would like to see different designs incorporated into the backside of the card. File 5,6,and 7 are ideas that I would like to see done with my business name. The diamond around my name with the polisher coming around the bottom, and a Veltrano outline on the left side of the diamond kinda like file 5
• Also, business name and name should be in some style of script, while the rest of the fonts in serif. Must have the picture of me on the front right side of the card!!!
Nice to have
• Your own personal ideas that you think I am missing.
Should not have
• No grafitti, no generic logos around the business name like every other auto detail card on google.

```html
<!DOCTYPE html>
<html lang="en">
<head>
<meta charset="utf-8">
<title>Bright K's Auto Detailing — Business Cards</title>
<link href="https://fonts.googleapis.com/css2?family=Roboto:wght@400;500&family=Roboto+Condensed:wght@700&display=swap" rel="stylesheet">
<style>
  :root {
    --red: #ec1f27;
    --black: #000000;
    --card: #050505;
    --white: #f2f2f2;
    --grey-text: #d6d6d6;
    --page: #e2e2e2;
  }
  * { box-sizing: border-box; margin: 0; padding: 0; }
  html, body { width: 1200px; height: 960px; overflow: hidden; }
  body {
    background: var(--page);
    position: relative;
    font-family: "Roboto", Arial, sans-serif;
  }
  .card {
    position: absolute;
    width: 600px;
    height: 343px;
    border-radius: 18px;
    background: var(--card);
    overflow: hidden;
  }
  .card--front { left: 292px; top: 130px; }
  .card--back { left: 289px; top: 499px; }

  /* front */
  .photo-slot {
    position: absolute; inset: 0;
    clip-path: polygon(345px 0, 600px 0, 600px 343px, 432px 343px);
    background: linear-gradient(160deg, #2a2f3a 0%, #3d4658 35%, #8c98b0 52%, #2c3240 70%, #5d6678 100%);
  }
  .brand {
    position: absolute; left: 44px; top: 62px;
    display: flex; align-items: center; gap: 10px;
  }
  .brand__mark { width: 12px; height: 12px; border-radius: 50%; background: var(--red); flex: none; }
  .brand__name {
    font-family: "Roboto", Arial, sans-serif;
    font-weight: 500;
    font-size: 27px;
    line-height: 1.15;
    color: var(--red);
    width: 240px;
  }
  .services { position: absolute; left: 50px; top: 155px; }
  .services__title {
    font-family: "Roboto Condensed", Arial, sans-serif;
    font-weight: 700; font-size: 16px; color: var(--red);
    letter-spacing: 0.2px; margin-bottom: 1px;
  }
  .services__list { list-style: none; }
  .services__list li {
    font-size: 14px; color: var(--grey-text); line-height: 20px;
    position: relative; padding-left: 15px;
  }
  .services__list li::before {
    content: ""; position: absolute; left: 1px; top: 8px;
    width: 5px; height: 5px; border-radius: 50%; background: var(--red);
  }

  /* back */
  .car-slot {
    position: absolute; inset: 0;
    background:
      radial-gradient(ellipse 26% 16% at 70% 58%, #262626 0%, rgba(20,20,20,0.6) 60%, transparent 100%),
      radial-gradient(ellipse 40% 8% at 70% 75%, #1e1e1e 0%, transparent 100%);
  }
  .person { position: absolute; left: 49px; top: 67px; }
  .person__name {
    font-family: "Roboto Condensed", Arial, sans-serif;
    font-weight: 700; font-size: 23px; color: var(--red); line-height: 1.1;
  }
  .person__role { font-size: 15px; font-weight: 500; color: var(--white); margin-top: 4px; }
  .contact { position: absolute; left: 50px; top: 141px; list-style: none; }
  .contact li {
    display: flex; align-items: center; gap: 8px;
    font-size: 14px; color: var(--white); line-height: 20.5px;
  }
  .contact svg { width: 14px; height: 14px; fill: var(--red); flex: none; }
  .social {
    position: absolute; left: 51px; top: 247px;
    display: flex; align-items: center; gap: 8px;
    font-size: 14px; color: var(--white);
  }
  .social__mark { width: 13px; height: 13px; background: var(--red); border-radius: 2px; }
</style>
</head>
<body>

<section class="card card--front">
  <div class="photo-slot" role="img" aria-label="Photo of the owner polishing a car with a buffer, lit by a bright garage light"></div>
  <div class="brand">
    <span class="brand__mark"></span>
    <span class="brand__name">Bright K's Auto Detailing</span>
  </div>
  <div class="services">
    <h2 class="services__title">SERVICES OFFERED</h2>
    <ul class="services__list">
      <li>Paint Correction</li>
      <li>Exterior detailing</li>
      <li>Interior Detailing</li>
      <li>Engine Bay Detailing</li>
      <li>Headlight restoration</li>
      <li>Ceramic Coatings</li>
    </ul>
  </div>
</section>

<section class="card card--back">
  <div class="car-slot" role="img" aria-label="Dark photo of a Veltrano sports car front under a spotlight"></div>
  <div class="person">
    <h1 class="person__name">COLIN MARCHETTI</h1>
    <p class="person__role">OWNER/ OPERATOR</p>
  </div>
  <ul class="contact">
    <li><svg viewBox="0 0 24 24"><path d="M12 1a8 8 0 0 0-8 8c0 6 8 14 8 14s8-8 8-14a8 8 0 0 0-8-8zm0 11a3 3 0 1 1 0-6 3 3 0 0 1 0 6z"/></svg>Oakmere, CA</li>
    <li><svg viewBox="0 0 24 24"><path d="M6.6 10.8a15 15 0 0 0 6.6 6.6l2.2-2.2a1 1 0 0 1 1-.25 11.4 11.4 0 0 0 3.6.6 1 1 0 0 1 1 1V20a1 1 0 0 1-1 1A17 17 0 0 1 3 4a1 1 0 0 1 1-1h3.5a1 1 0 0 1 1 1c0 1.25.2 2.45.6 3.6a1 1 0 0 1-.25 1z"/></svg>(559) 214-6079</li>
    <li><svg viewBox="0 0 24 24"><path d="M2 5h20v14H2zm2 2v.5l8 5 8-5V7l-8 5z"/></svg>colin@thebrightpolisher.example</li>
    <li><svg viewBox="0 0 24 24"><path d="M12 2a10 10 0 1 0 0 20 10 10 0 0 0 0-20zm0 3a7 7 0 0 1 6.9 6h-4a13 13 0 0 0-1.5-5.8A7 7 0 0 1 12 5zm-2 14a7 7 0 0 1-4.9-6h4a13 13 0 0 0 1.2 6z"/></svg>thebrightpolisher.example</li>
  </ul>
  <div class="social">
    <span class="social__mark"></span>
    <span>@thebrightpolisher</span>
  </div>
</section>

</body>
</html>
```